Seeking Talented PSD Designer for Real Estate Finance Web Site

Hello ...
Need a minimalist design for a high - end finance web site that conveys prestige / sophistication / class ... Below are comps for this project ...
http://www.tawnyridgefunding.com/
http://glenmoorfunds.com/
http://www.cedarloftfp.com/
http://halvornfunds.com/
Look forward too receiving proposals for this project ....
Target Market(s)
Commerciale entities seeking more than $500.0 k in interim capital ... These could include apartment owners / construction managers / restaurant owners / hotels / golf courses ...
Industry/Entity Type
Real Estate
Number of Pages Required
1 page
Requirements
Must have
- Super high quality graphic design ... Has to be marketable and convert customers to contact us ...
- Please refer to logo concept four ....
Should not have
- clunky / poor fonts /

```html
<!DOCTYPE html>
<html lang="en">
<head>
<meta charset="utf-8">
<title>Ashgrove Capital</title>
<link rel="stylesheet" href="https://fonts.googleapis.com/css2?family=Carlito:wght@400;700&family=Montserrat:wght@500;600&family=Raleway:wght@500&display=swap">
<style>
:root{
  --ink:#ffffff;
  --ink-soft:#e6e6e6;
  --rule:rgba(255,255,255,.45);
  --navy:#2d3f6b;
  --footer:#2b3552;
  --night-top:#1c1c1e;
  --night-mid:#2a2a2c;
  --night-low:#141416;
  --logo-grey:#b9b9bb;
}
*{margin:0;padding:0;box-sizing:border-box}
html,body{width:1200px;height:841px;overflow:hidden;background:#000}
body{position:relative;font-family:"Carlito",sans-serif;color:var(--ink)}
.hero-photo{
  position:absolute;left:0;top:0;width:1200px;height:747px;
  background:
    linear-gradient(180deg,rgba(0,0,0,0) 55%,rgba(0,0,0,.55) 85%,rgba(10,10,12,.8) 100%),
    radial-gradient(ellipse at 55% 30%,var(--night-mid) 0%,var(--night-top) 55%,var(--night-low) 100%);
}
.brand{position:absolute;left:52px;top:21px;width:220px;text-align:center}
.brand-mark{display:block;width:80px;height:80px;margin:0 auto 14px;border-radius:50%;background:var(--logo-grey)}
.brand-name{font-family:"Montserrat",sans-serif;font-weight:500;font-size:22px;letter-spacing:4px;color:var(--logo-grey);line-height:1.2}
.call{position:absolute;right:49px;top:46px;display:flex;align-items:center;gap:10px}
.call-text{text-align:right;line-height:1.15}
.call-label{font-size:12.5px}
.call-number{font-size:16px;font-weight:700}
.call-icon{width:39px;height:39px;border:1.5px solid var(--ink);border-radius:50%;display:flex;align-items:center;justify-content:center}
.main-nav{position:absolute;left:47px;top:264px;width:284px}
.main-nav a{display:block;height:76px;padding-left:38px;line-height:42px;font-family:"Raleway",sans-serif;font-weight:500;font-size:16px;color:var(--ink);text-decoration:none;border-bottom:1px solid var(--rule)}
.main-nav a:first-child{height:55px;line-height:42px}
.intro{position:absolute;left:442px;top:334px;width:625px}
.intro-title{font-family:"Montserrat",sans-serif;font-weight:600;font-size:34px;letter-spacing:.5px;line-height:42px}
.intro-rule{height:2px;margin:7px 0 14px 4px;background:linear-gradient(90deg,var(--ink-soft),rgba(255,255,255,.3))}
.intro-text{font-size:15.5px;line-height:22.7px;color:var(--ink-soft)}
.read-more{display:inline-block;margin:23px 0 0 5px;width:132px;height:43px;line-height:41px;text-align:center;background:var(--navy);border:1px solid var(--ink);font-size:12.5px;color:var(--ink);text-decoration:none}
.site-footer{position:absolute;left:0;top:747px;width:1200px;height:94px;background:var(--footer)}
.copyright{position:absolute;left:49px;top:37px;font-size:12.5px;color:var(--ink-soft)}
.social{position:absolute;right:49px;top:28px;display:flex;gap:18px}
.social a{width:38px;height:38px;border-radius:50%;border:1.5px solid var(--ink)}
.social a.is-active{background:var(--ink)}
</style>
</head>
<body>
<div class="hero-photo" role="img" aria-label="Dusky city skyline with a gothic clock tower and parliament buildings, in dark grey tones"></div>

<header>
  <div class="brand">
    <span class="brand-mark" aria-hidden="true"></span>
    <div class="brand-name">ASHGROVE CAPITAL</div>
  </div>
  <div class="call">
    <div class="call-text">
      <div class="call-label">CALL US</div>
      <div class="call-number">+123-456-7890</div>
    </div>
    <div class="call-icon">
      <svg width="20" height="20" viewBox="0 0 24 24" fill="#fff" aria-hidden="true"><path d="M6.6 10.8a15.1 15.1 0 0 0 6.6 6.6l2.2-2.2a1 1 0 0 1 1-.25 11.4 11.4 0 0 0 3.6.57 1 1 0 0 1 1 1V20a1 1 0 0 1-1 1A17 17 0 0 1 3 4a1 1 0 0 1 1-1h3.5a1 1 0 0 1 1 1c0 1.25.2 2.45.57 3.6a1 1 0 0 1-.25 1z"/></svg>
    </div>
  </div>
</header>

<nav class="main-nav">
  <a href="#">HOME</a>
  <a href="#">ABOUT US</a>
  <a href="#">TRANSACTIONS</a>
  <a href="#">LOAN</a>
  <a href="#">CONTACT US</a>
</nav>

<main class="intro">
  <h1 class="intro-title">ASHGROVE CAPITAL</h1>
  <div class="intro-rule"></div>
  <p class="intro-text">Lorem ipsum dolor sit amet, consectetur adipiscing elit, sed do eiusmod tempor incididunt ut labore et doloreLorem ipsum dolor sit amet, consectetur adipiscing elit, sed do eiusmod tempor incididunt ut labore et dolore</p>
  <a class="read-more" href="#">READ MORE</a>
</main>

<footer class="site-footer">
  <p class="copyright">All Right Reserved. Copyright ©2016 Ashgrove Capital</p>
  <div class="social">
    <a href="#" class="is-active" aria-label="Social profile one"></a>
    <a href="#" aria-label="Social profile two"></a>
    <a href="#" aria-label="Social profile three"></a>
  </div>
</footer>
</body>
</html>
```